Reed & Vale NC grand opening (for BILLBOARD)

Advertising the grand opening of our cannabis/hemp shop in NC. We will sell all things hemp (flower, cartridges, disposables, edibles, creams, lotions, pet products etc...)

Requirements
Must have
• include, open starting Aug 1, but grand opening Aug 15th.
Nice to have
• Difference slogan ideas "Save some cash, buy our grass" "Find your perfect high at Reed & Vale cannabis store" "Experience Nature's Gift: Reed & Vale Cannabis Store"

```html
<!DOCTYPE html>
<html lang="en">
<head>
<meta charset="utf-8">
<title>Reed &amp; Vale – Grand Opening Billboard</title>
<link rel="stylesheet" href="https://fonts.googleapis.com/css2?family=Montserrat:wght@300;400;600;800&family=Cinzel:wght@400;600&family=Great+Vibes&display=swap">
<style>
  :root {
    --navy: #141a3c;
    --green: #7cc242;
    --green-dark: #1f7a35;
    --white: #ffffff;
    --page: #ececec;
    --skin: #d9a98c;
    --shirt: #d42a24;
  }
  html, body {
    margin: 0;
    width: 1200px;
    height: 1170px;
    overflow: hidden;
    background: var(--page);
  }
  .billboard {
    position: absolute;
    left: 0;
    top: 410px;
    width: 1200px;
    height: 349px;
    background: var(--white);
    overflow: hidden;
    font-family: "Montserrat", sans-serif;
    color: var(--navy);
  }
  .leaf-mark {
    position: absolute;
    background: radial-gradient(circle, var(--green) 0%, var(--green-dark) 70%, transparent 71%);
  }
  .leaf-mark--top { left: 3px; top: 4px; width: 121px; height: 120px; }
  .leaf-mark--bottom { left: 12px; top: 275px; width: 62px; height: 59px; }

  .brand {
    position: absolute;
    left: 150px;
    width: 380px;
    top: 62px;
    text-align: center;
    font-weight: 600;
    font-size: 58px;
    line-height: 1;
    color: var(--navy);
    letter-spacing: -1px;
  }
  .slogan {
    position: absolute;
    left: 40px;
    width: 600px;
    top: 156px;
    text-align: center;
    margin: 0;
  }
  .slogan__bold {
    display: block;
    font-weight: 800;
    font-size: 56px;
    line-height: 51px;
  }
  .slogan__light {
    display: block;
    font-weight: 300;
    font-size: 56px;
    line-height: 51px;
  }
  .location-rule {
    position: absolute;
    top: 293px;
    height: 3px;
    background: var(--green);
  }
  .location-rule--left { left: 73px; width: 75px; }
  .location-rule--right { left: 532px; width: 79px; }
  .location {
    position: absolute;
    left: 155px;
    top: 275px;
    width: 370px;
    height: 37px;
    background: var(--green);
    color: var(--navy);
    font-size: 19px;
    font-weight: 400;
    line-height: 37px;
    text-align: center;
  }
  .location strong { font-weight: 800; }

  .event-panel {
    position: absolute;
    left: 884px;
    top: 0;
    width: 316px;
    height: 349px;
    background: var(--navy);
  }
  .promo-photo {
    position: absolute;
    left: 642px;
    top: 0;
    width: 242px;
    height: 349px;
    background: linear-gradient(160deg, var(--green) 0%, var(--green-dark) 30%, var(--skin) 55%, var(--shirt) 85%);
    border-radius: 121px 121px 0 0;
  }
  .event {
    position: absolute;
    left: 900px;
    width: 290px;
    top: 0;
    height: 349px;
    color: var(--white);
    text-align: center;
  }
  .event > * {
    position: absolute;
    left: 0;
    width: 290px;
    margin: 0;
  }
  .event__title {
    top: 26px;
    font-family: "Cinzel", serif;
    font-weight: 600;
    font-size: 64px;
    line-height: 66px;
  }
  .event__script {
    top: 78px;
    font-family: "Great Vibes", cursive;
    font-size: 80px;
    line-height: 80px;
    color: var(--green);
  }
  .event__rule {
    top: 171px;
    left: 130px;
    width: 30px;
    height: 2px;
    background: var(--white);
  }
  .event__details {
    top: 204px;
    font-family: "Cinzel", serif;
    font-size: 18px;
    line-height: 22px;
  }
  .event__date {
    top: 273px;
    font-family: "Cinzel", serif;
    font-size: 28px;
    line-height: 32px;
    color: var(--green);
  }
</style>
</head>
<body>
  <section class="billboard">
    <div class="leaf-mark leaf-mark--top" role="img" aria-label="Green cannabis leaf illustration"></div>
    <div class="leaf-mark leaf-mark--bottom" role="img" aria-label="Small green cannabis leaf illustration"></div>

    <div class="brand">Reed &amp; Vale</div>

    <h1 class="slogan">
      <span class="slogan__bold">SAVE SOME CASH,</span>
      <span class="slogan__light">BUY OUR GRASS</span>
    </h1>

    <span class="location-rule location-rule--left"></span>
    <div class="location">*<strong>OFF EXIT</strong> 4B MILLBROOK RD</div>
    <span class="location-rule location-rule--right"></span>

    <div class="event-panel"></div>
    <div class="promo-photo" role="img" aria-label="Photo of an excited woman in a red shirt holding a fan of cash and making an OK sign, framed by large green leaves"></div>

    <div class="event">
      <h2 class="event__title">GRAND</h2>
      <span class="event__script">Opening</span>
      <span class="event__rule"></span>
      <p class="event__details">OPEN STARTING<br>AUG 1, BUT GRAND<br>OPENING</p>
      <p class="event__date">AUG 15TH.</p>
    </div>
  </section>
</body>
</html>
```